Business Catalog - Skincare Clinic

We are skincare clinic and specialize in treating chronic Skin diseases like Psoriasis and Eczema. We also sell evidence based treatment medicine which are natural, bio- herbal.

We are in need of a brochure which will promote our clinic and treatment options to clients.

It will be around 10 - 12 pages and will involve a catchy cover and attractive design template. Will need to keep to Blue/ Aqua blue color and look scientific.

Content material will be provided. Attached is the sample of our European region catalog. However the one we are developing will have to small in number of pages as well as blue in color. This is only a sample for indication and you are free to design it as per your creative thoughts.

Our website is www.brivelhealth.com.au, www.dermoralia.com.au

About Us
We are a leader in complimentary dermatology. With over 30 years of medical research & clinical practice, Vashel Fairbrook Clinic is dedicated to on-going research to help our patients achieve the best possible results.

We have specialised in the treatment of Psoriasis and Eczema. Focusing and researching on these diseases for the last many decades have given us extensive understanding of the causes of the disease. We have treated more than 125,000 patients in Australia. Through these experiences in treating patient at our clinic, we have designed unique treatment protocols, which addresses the triggers of the disease and thus effectively treating symptom. We have developed products which supports this protocols and act very effective in bringing solution to the disease. All our product are based on plant actives, extracts and thus considered to be extremely safe. The treatment protocol along with our products have been validated for their effectiveness through numerous clinical trials conducted on them in Australia, Europe, Russia and Asian countries.
Updates

Project Deadline Extended
Reason: We have still not received any design which satisfies our requiement

Industry/Entity Type

Clinic

```html
<!DOCTYPE html>
<html lang="en">
<head>
<meta charset="utf-8">
<title>Halden Marsh Dermaceuticals – About Us Spread</title>
<link rel="stylesheet" href="https://fonts.googleapis.com/css2?family=Montserrat:wght@400;600&family=Open+Sans:ital,wght@0,400;0,600;1,400;1,600&display=swap">
<style>
  :root {
    --bg: #e9ebed;
    --paper: #f7f8f9;
    --teal: #5fb8bf;
    --blue: #2d8fc9;
    --blue-dark: #1f6fa3;
    --grey-text: #6f7479;
    --grey-dark: #4a4f55;
    --photo-light: #e4e6e8;
    --photo-dark: #9a9ea3;
  }
  * { margin: 0; padding: 0; box-sizing: border-box; }
  html, body { width: 1200px; height: 778px; overflow: hidden; background: var(--bg); }
  body { position: relative; font-family: "Open Sans", Arial, sans-serif; }

  .brand {
    position: absolute; left: 130px; top: 138px;
    display: flex; align-items: center; gap: 12px;
  }
  .brand-dot { width: 34px; height: 34px; border-radius: 50%; background: var(--blue); }
  .brand-name {
    font-family: "Montserrat", Arial, sans-serif; font-weight: 400;
    color: var(--blue); font-size: 27px; line-height: 1.05;
  }
  .brand-name small { display: block; font-size: 13px; letter-spacing: 5px; }

  .spread {
    position: absolute; left: 70px; top: 240px; width: 1060px; height: 460px;
    display: flex; box-shadow: 0 10px 28px rgba(0,0,0,.18);
  }
  .page { position: relative; width: 530px; height: 460px; background: var(--paper); overflow: hidden; }
  .page-left { border-top: 5px solid var(--teal); }
  .page-right { border-top: 5px solid var(--teal); }

  .hero-photo {
    position: absolute; inset: 0;
    background: radial-gradient(ellipse at 65% 45%, var(--photo-light) 0%, #c7cacd 45%, var(--photo-dark) 100%);
  }
  .about-badge {
    position: absolute; left: 30px; top: 120px; width: 180px; height: 180px; border-radius: 50%;
    background: var(--blue); border: 4px solid #fff; color: #fff;
    display: flex; flex-direction: column; align-items: center; justify-content: center;
    text-align: center; padding: 0 22px;
  }
  .about-badge h2 {
    font-family: "Montserrat", Arial, sans-serif; font-weight: 400; font-size: 19px; letter-spacing: 1px; margin-bottom: 6px;
  }
  .about-badge p { font-size: 7.4px; line-height: 1.45; }
  .about-badge strong { font-weight: 600; }

  .folio-mark {
    position: absolute; bottom: 18px; display: flex; align-items: center; gap: 4px;
    font-family: "Montserrat", Arial, sans-serif; font-size: 8px; color: var(--blue);
  }
  .folio-mark i { width: 8px; height: 8px; border-radius: 50%; background: var(--blue); display: block; }
  .page-left .folio-mark { right: 24px; }
  .page-right .folio-mark { left: 36px; }

  .section-tab {
    position: absolute; right: 30px; top: 0; background: var(--teal); color: #fff;
    font-family: "Montserrat", Arial, sans-serif; font-size: 9px; letter-spacing: 1px; padding: 5px 14px;
  }
  .content { position: absolute; left: 36px; top: 42px; width: 450px; }
  .content h1 {
    font-family: "Open Sans", Arial, sans-serif; font-style: italic; font-weight: 600;
    color: var(--blue); font-size: 26px; margin-bottom: 8px;
  }
  .lead-q { font-style: italic; font-size: 10px; color: var(--grey-dark); margin-bottom: 10px; }
  .lead { font-style: italic; font-weight: 600; font-size: 10px; line-height: 1.55; color: var(--blue); margin-bottom: 14px; }
  .body-copy p { font-size: 8.6px; line-height: 1.65; color: var(--grey-text); margin-bottom: 10px; }
  .body-copy .link { color: var(--blue); }
  .page-number { position: absolute; right: 30px; bottom: 18px; font-size: 9px; color: var(--teal); }
</style>
</head>
<body>
  <div class="brand">
    <span class="brand-dot"></span>
    <div class="brand-name">Halden Marsh<small>DERMACEUTICALS</small></div>
  </div>

  <div class="spread">
    <section class="page page-left">
      <div class="hero-photo" role="img" aria-label="Black and white photograph of a mother cuddling her smiling baby on a bed"></div>
      <div class="about-badge">
        <h2>ABOUT US</h2>
        <p>While an ‘over the counter’ cream may give you some relief, the best long-term treatment for your skin is a customised solution. At the Vashel Fairbrook Clinic we take a holistic approach and <strong>develop a personalised treatment protocol for YOU.</strong></p>
      </div>
      <div class="folio-mark"><i></i>Halden Marsh</div>
    </section>

    <section class="page page-right">
      <div class="section-tab">ABOUT US</div>
      <div class="content">
        <h1>Introduction</h1>
        <p class="lead-q">At Vashel Fairbrook Clinic we practice Complementary Dermatology. So what does that mean?</p>
        <p class="lead">Complementary and alternative medicine (CAM) in dermatology encompasses a wide variety of methods of diagnosis and treatment that either supplement or substitute for conventional methods. Our practice draws on an expanded knowledge base and the latest research findings, combining these approaches in what might also be termed integrative dermatology.</p>
        <div class="body-copy">
          <p>Our approach combines proven scientific research with plant-based therapies. Rather than masking symptoms, we look for the underlying triggers of each condition and treat them directly, so that relief lasts longer and flare-ups become less frequent over time.</p>
          <p>Every patient begins with a detailed consultation. We review medical history, diet, stress and lifestyle, then build a tailored program of topical care, supplements and practical changes to support healthy skin.</p>
          <p>Dr. Marsh founded the clinic after years of research into psoriasis and eczema, and the team continues to refine its <span class="link">treatment protocols</span> through ongoing clinical study and patient feedback.</p>
        </div>
      </div>
      <div class="folio-mark"><i></i>Halden Marsh</div>
      <span class="page-number">3</span>
    </section>
  </div>
</body>
</html>
```